Birchfall Kennels

create website page for Labrador Retriever stud dog business.

Target Market(s)

Owners looking to breed their dogs that compete in NFR/DSG hunt tests.

Industry/Entity Type

Dog Training

Logo Text

Birchfall Kennals - Stud Dogs

Number of Pages Required

1 page

Colors

Designer to choose colors to be used in the design.

Requirements
Must have
• link to or info from my dogs pedigree.
• Main dog I'm advertising. HRCH Pip's Whistle 4 Rounds MH
• http://www.fieldpupregistry.example/pedigree.asp?id=71926
• also link to gundog tallies-- for pass information.
• Can update the pictures to that actual pictures once design is complete.

```html
<!DOCTYPE html>
<html lang="en">
<head>
<meta charset="utf-8">
<title>Birchfall Kennels – Labrador Retriever Stud Dogs</title>
<link href="https://fonts.googleapis.com/css2?family=Raleway:wght@400;500;600;700;800&display=swap" rel="stylesheet">
<style>
  :root {
    --gold: #f2c53a;
    --gold-deep: #c9962e;
    --sand: #dcc68a;
    --sand-light: #e8d49e;
    --wood: #a3663b;
    --wood-dark: #7e4a27;
    --ink: #1e1a14;
    --heading: #4a3520;
    --nav-bg: rgba(30, 30, 30, 0.78);
    --forest: #37412f;
    --forest-dark: #2b3326;
    --white: #ffffff;
    --field: #dfe0dc;
    --accent-green: #4cd964;
    --rust: #c0692e;
  }
  * { box-sizing: border-box; margin: 0; padding: 0; }
  html, body {
    width: 1200px; height: 1200px; overflow: hidden;
    background: var(--white);
    font-family: "Raleway", sans-serif;
  }
  .page {
    position: absolute; left: 166px; top: 0;
    width: 870px; height: 1200px; overflow: hidden;
  }
  .abs { position: absolute; }

  /* Hero */
  .hero {
    left: 0; top: 0; width: 870px; height: 494px;
    background: linear-gradient(180deg, #8f8b7e 0%, #7d8288 30%, #a8987a 55%, #8d9199 70%, #a9adb2 100%);
  }
  .title-band {
    left: 0; top: 0; width: 870px; height: 38px;
    background: linear-gradient(180deg, #8a6a3a, #b48a4c);
  }
  .site-title {
    left: 0; top: 4px; width: 870px; text-align: center;
    color: var(--gold); font-weight: 700; font-size: 21px; letter-spacing: 0.2px;
  }
  .nav {
    left: 0; top: 38px; width: 870px; height: 40px;
    background: var(--nav-bg);
  }
  .nav a {
    position: absolute; top: 14px; color: var(--white);
    font-size: 9.5px; font-weight: 700; text-decoration: none;
  }
  .nav a.current { color: var(--gold); }
  .brand {
    left: 42px; top: 8px; width: 100px; height: 100px; border-radius: 50%;
    background: radial-gradient(circle at 40% 35%, #f6dc85, var(--gold-deep));
    border: 2px solid #3a2b14;
    display: flex; align-items: center; justify-content: center; text-align: center;
    color: var(--ink); font-weight: 800; font-size: 11px; line-height: 1.2;
  }

  /* Content */
  .content {
    left: 0; top: 494px; width: 870px; height: 444px;
    background: var(--sand); border-top: 2px solid #9a7440;
  }
  .h2 {
    color: var(--heading); font-weight: 700; font-size: 21px;
    text-shadow: 1px 1px 0 rgba(255,255,255,0.35);
  }
  .body-text {
    color: #2e2618; font-size: 11px; line-height: 15.5px; text-align: justify;
  }
  .news { list-style: none; }
  .news li {
    position: absolute; left: 0; font-size: 11px; color: #2e2618; line-height: 15.5px;
    padding-left: 20px; width: 270px; text-align: justify;
  }
  .news li::before {
    content: "›"; position: absolute; left: 2px; top: -1px;
    color: var(--rust); font-weight: 800; font-size: 13px;
  }

  .wood {
    background: repeating-linear-gradient(90deg, var(--wood) 0 14px, #9b5f35 14px 17px, #a86c40 17px 30px);
  }
  .photo {
    border: 2px solid var(--gold); border-radius: 4px;
  }
  .promo-title { color: var(--gold); font-size: 6.5px; font-weight: 700; }
  .promo-text { color: #f0dcc0; font-size: 6.5px; line-height: 8px; text-align: justify; }
  .btn-small {
    background: var(--gold); color: var(--ink); font-size: 6.5px; font-weight: 800;
    display: flex; align-items: center; justify-content: center; border-radius: 2px;
  }

  .tabs { left: 336px; top: 550px; width: 495px; height: 30px; background: #111; border: 1px solid #000; }
  .tab {
    position: absolute; top: 0; height: 28px; width: 107px;
    color: #f4e4b0; font-size: 7px; font-weight: 800;
    display: flex; align-items: center; justify-content: center;
  }
  .tab.active { background: #0c0c0c; color: var(--gold); }
  .tab.soft { background: linear-gradient(90deg, #a3663b, #6a4428 70%, #111); }

  .card-title { color: var(--gold); font-weight: 700; font-size: 14px; }
  .card-text { color: #fbeedd; font-size: 9px; line-height: 13.6px; width: 278px; }
  .read-more { color: var(--white); font-size: 9px; font-weight: 500; }
  .read-more span { color: var(--accent-green); font-weight: 800; }

  /* Footer */
  .footer {
    left: 0; top: 938px; width: 870px; height: 262px;
    background: linear-gradient(180deg, var(--forest) 0%, #3f4a36 60%, var(--forest-dark) 100%);
  }
  .f-head { color: var(--white); font-weight: 700; font-size: 15px; text-shadow: 1px 1px 1px rgba(0,0,0,0.5); }
  .f-text { color: #ecefe6; font-size: 10.5px; line-height: 15.5px; text-align: justify; width: 248px; }
  .f-info { color: #ecefe6; font-size: 9.6px; font-weight: 600; line-height: 16px; }
  .btn-sand {
    background: var(--sand-light); border-radius: 3px; color: var(--rust);
    display: flex; align-items: center; justify-content: center; font-weight: 700;
  }
  .field {
    background: var(--field); color: #4b4b4b; font-size: 10px; font-weight: 600;
    padding-left: 10px; display: flex; align-items: center;
  }
  .social { width: 28px; height: 28px; border-radius: 50%; border: 2px solid #2a2a2a; }
  .legal { color: #ecefe6; font-size: 8px; font-weight: 700; }
</style>
</head>
<body>
<div class="page">

  <!-- Hero -->
  <div class="abs hero" role="img" aria-label="Black Labrador retriever wading through shallow water carrying a duck, with golden marsh grass behind"></div>
  <div class="abs title-band"></div>
  <div class="abs site-title">LABRADOR RETRIEVER STUD DOG BUSINESS</div>
  <nav class="abs nav">
    <a class="current" style="left:300px">HOME</a>
    <a style="left:351px">ABOUT</a>
    <a style="left:409px">EVENTS</a>
    <a style="left:469px">GALLERY</a>
    <a style="left:534px">CONTACT US</a>
  </nav>
  <div class="abs brand">BIRCHFALL<br>KENNELS</div>

  <!-- Content -->
  <section class="abs content"></section>

  <h2 class="abs h2" style="left:45px; top:514px">ABOUT US</h2>
  <p class="abs body-text" style="left:44px; top:552px; width:270px">Lorem ipsum dolor sit amet, consectetur adipiscing elit, sed do eiusmod tempor incididunt ut labore et dolore magna aliqua. Ut enim ad minim veniam, quis nostrud exercitation ullamco laboris nisi ut aliquip ex ea commodo consequat.</p>

  <h2 class="abs h2" style="left:43px; top:654px; font-size:20px">NEWS &amp; ANNOUNCEMENTS</h2>
  <ul class="abs news" style="left:44px; top:0">
    <li style="top:688px">sed do eiusmod tempor incididunt ut labore</li>
    <li style="top:707px">Nemo enim ipsam voluptatem quia voluptas sit aspernatur aut odit aut fugit</li>
    <li style="top:740px">sed do eiusmod tempor incididunt ut labore</li>
    <li style="top:758px">sed do eiusmod tempor incididunt ut labore</li>
  </ul>

  <div class="abs wood" style="left:43px; top:794px; width:281px; height:101px"></div>
  <div class="abs photo" style="left:55px; top:811px; width:99px; height:67px; background:linear-gradient(135deg,#4a5a6a,#2a2f38 50%,#8a5a3a)" role="img" aria-label="Black Labrador holding a pheasant"></div>
  <div class="abs promo-title" style="left:164px; top:811px">HUNTING SUPPLIES – PRODUCT CATEGORIES</div>
  <p class="abs promo-text" style="left:164px; top:823px; width:144px">Ut enim ad minim veniam, quis nostrud exercitation ullamco laboris nisi ut aliquip ex ea commodo consequat.</p>
  <div class="abs btn-small" style="left:256px; top:856px; width:52px; height:14px">VIEW MORE</div>

  <h2 class="abs h2" style="left:340px; top:514px">SERVICES</h2>
  <div class="abs tabs">
    <div class="tab active" style="left:0">HUNT TEST TRAINING</div>
    <div class="tab soft" style="left:107px">ADVANCED GUN DOG</div>
    <div class="tab" style="left:214px">OBEDIENCE TRAINING</div>
    <div class="tab" style="left:321px">HUNT TEST TRAINING</div>
  </div>

  <div class="abs wood" style="left:336px; top:594px; width:495px; height:146px"></div>
  <div class="abs photo" style="left:353px; top:614px; width:155px; height:104px; background:linear-gradient(135deg,#d9b870,#a08048)" role="img" aria-label="Portrait of a black Labrador retriever"></div>
  <h3 class="abs card-title" style="left:524px; top:614px">BASIC TRAINING</h3>
  <p class="abs card-text" style="left:525px; top:645px">At vero eos et accusamus et iusto odio dignissimos ducimus qui blanditiis praesentium voluptatum deleniti atque corrupti quos dolores et quas molestias excepturi sint occaecati cupiditate non provident, similique sunt in culpa qui officia deserunt mollitia animi, id est laborum et dolorum fuga.</p>
  <div class="abs read-more" style="left:736px; top:717px">Read More <span>»</span></div>

  <div class="abs wood" style="left:336px; top:749px; width:495px; height:146px"></div>
  <div class="abs photo" style="left:353px; top:770px; width:155px; height:102px; background:linear-gradient(135deg,#8d8060,#b0aca0 50%,#9a7a58)" role="img" aria-label="Black Labrador running through splashing water in a marsh"></div>
  <h3 class="abs card-title" style="left:525px; top:768px">ADVANCED TRAINING</h3>
  <p class="abs card-text" style="left:525px; top:797px">At vero eos et accusamus et iusto odio dignissimos ducimus qui blanditiis praesentium voluptatum deleniti atque corrupti quos dolores et quas molestias excepturi sint occaecati cupiditate non provident, similique sunt in culpa qui officia deserunt mollitia animi, id est laborum et dolorum fuga.</p>
  <div class="abs read-more" style="left:736px; top:865px">Read More <span>»</span></div>

  <!-- Footer -->
  <footer class="abs footer"></footer>

  <h4 class="abs f-head" style="left:43px; top:955px">ABOUT US</h4>
  <p class="abs f-text" style="left:43px; top:988px">Lorem ipsum dolor sit amet, consectetur adipiscing elit, sed do eiusmod tempor incididunt ut labore et dolore magna aliqua. Ut enim ad minim veniam, quis nostrud exercitation ullamco laboris nisi ut aliquip ex ea commodo consequat.</p>
  <div class="abs btn-sand" style="left:43px; top:1076px; width:101px; height:31px; font-size:10px">READ MORE&nbsp;&nbsp;»</div>

  <h4 class="abs f-head" style="left:319px; top:955px">CONTACT NOW</h4>
  <svg class="abs" style="left:319px; top:994px" width="17" height="13" viewBox="0 0 17 13">
    <rect x="1" y="1" width="15" height="11" fill="none" stroke="#fff" stroke-width="1.5"/>
    <polyline points="1,1 8.5,7 16,1" fill="none" stroke="#fff" stroke-width="1.5"/>
  </svg>
  <div class="abs f-info" style="left:346px; top:991px">INFO@BIRCHFALLKENNELS.EXAMPLE</div>
  <svg class="abs" style="left:321px; top:1017px" width="14" height="19" viewBox="0 0 14 19">
    <path d="M7 0C3.1 0 0 3.1 0 7c0 5 7 12 7 12s7-7 7-12c0-3.9-3.1-7-7-7z" fill="#fff"/>
    <circle cx="7" cy="7" r="2.6" fill="#37412f"/>
  </svg>
  <div class="abs f-info" style="left:346px; top:1017px">DE FINIBUS BONORUM ET MALORUM,<br>VOLUPTATEM ACCUSANTIUM,<br>DOLOREMQUE.</div>
  <div class="abs social" style="left:345px; top:1080px; background:#7c8a6a"></div>
  <div class="abs social" style="left:379px; top:1080px; background:#a3663b"></div>
  <div class="abs social" style="left:413px; top:1080px; background:#c9962e"></div>

  <h4 class="abs f-head" style="left:628px; top:955px">SEND MAIL NOW</h4>
  <div class="abs field" style="left:629px; top:989px; width:192px; height:29px">NAME</div>
  <div class="abs field" style="left:629px; top:1027px; width:192px; height:30px">EMAIL ADDRESS</div>
  <div class="abs btn-sand" style="left:629px; top:1076px; width:101px; height:31px; font-size:13px">SEND</div>

  <div class="abs legal" style="left:48px; top:1169px">TERMS &amp; CONDITIONS</div>
  <div class="abs legal" style="left:153px; top:1169px">|</div>
  <div class="abs legal" style="left:172px; top:1169px">PRIVACY &amp; SECURITY</div>
  <div class="abs legal" style="left:520px; top:1169px; width:311px; text-align:right">COPY RIGHTS RESERVED @ 2017 BIRCHFALL KENNELS</div>

</div>
</body>
</html>
```